Business Cards & Stationery for Tree Service Company
The Branch Mender
Business Cards & Stationery for Tree Service Company - Outdoors
Creative Brief
Use same font as used in my logo
It doesn't matter if you use the same font as long as it looks good I am up for creativity.
Professional
Wade Pellow
President
4817 Ransome Ave Suite 100 Des Moines, IA 50321
info@branchmenderpro.com
www.branchmenderpro.com
I would like some form of "dot" used to separate the phone and fax #'s as I think it looks cleaner and more modern. Aside from that I am looking for something cool/hip while staying clean and professional. I also need this design to be able to be edited as I need to make cards for all of my employees.
I am unaware of the proper way to make a double sided business card so I am up for the traditional way or originality whichever you prefer. I put QR Codes on a business card in the past so if you are open to ideas and you need my help for something please let me know.

```html
<!DOCTYPE html>
<html lang="en">
<head>
<meta charset="utf-8">
<title>The Branch Mender — Stationery</title>
<link href="https://fonts.googleapis.com/css2?family=Montserrat:wght@400;600;800&display=swap" rel="stylesheet">
<style>
:root{
  --bg:#e4e6e9;
  --paper:#ffffff;
  --navy:#0b2a6b;
  --blue:#1656c4;
  --sky:#4aa3ee;
  --green:#5a9e2f;
  --ink:#2b3440;
  --muted:#6b7480;
  --flap:#eceef1;
}
*{margin:0;padding:0;box-sizing:border-box}
html,body{width:1200px;height:814px;overflow:hidden;background:var(--bg);font-family:"Montserrat",sans-serif;color:var(--ink)}
.stage{position:relative;width:1200px;height:814px}
.sheet{position:absolute;background:var(--paper);box-shadow:0 6px 18px rgba(0,0,0,.18);overflow:hidden}
.sheet svg.swoosh{position:absolute;inset:0;width:100%;height:100%}
.brand{display:flex;align-items:center;gap:6px;position:absolute}
.brand-dot{width:14px;height:14px;border-radius:50%;background:var(--green);flex:none}
.brand-name{font-weight:800;color:var(--navy);white-space:nowrap}
.tagline{font-size:7px;color:var(--muted);letter-spacing:.5px;position:absolute}
.small{font-size:6px;line-height:1.5;color:var(--muted);position:absolute}

/* business cards */
.card{width:300px;height:172px;left:40px}
.card-back{top:210px}
.card-front{top:420px}
.card-front .lockup{position:absolute;left:44px;width:214px;top:68px;display:flex;flex-direction:column;align-items:center;gap:6px}
.card-front .brand{position:static}
.card-front .brand-dot{width:18px;height:18px}
.card-front .brand-name{font-size:13px}
.card-front .tagline{position:static}
.card-back .brand{left:30px;top:20px}
.card-back .brand-name{font-size:11px}
.person{position:absolute;left:30px;top:92px}
.person .name{font-size:11px;font-weight:600;color:var(--navy)}
.person .title{font-size:7px;color:var(--muted)}
.contacts{position:absolute;left:150px;top:52px;list-style:none}
.contacts li{display:flex;align-items:center;gap:6px;font-size:6.5px;color:var(--ink);margin-bottom:7px;max-width:130px;line-height:1.3}
.contacts .ico{width:8px;height:8px;border-radius:50%;background:var(--blue);flex:none}

/* letterhead */
.letterhead{left:380px;top:60px;width:400px;height:518px}
.letterhead .brand{right:28px;top:22px}
.letterhead .brand-name{font-size:12px}
.letterhead .small{right:28px;top:44px;text-align:right}

/* envelopes */
.envelope{left:820px;width:340px;height:170px}
.env-back{top:150px}
.env-front{top:370px}
.env-back .brand{left:128px;top:14px}
.env-back .brand-name{font-size:8px}
.env-back .brand-dot{width:9px;height:9px}
.env-front .brand{right:16px;top:16px}
.env-front .brand-name{font-size:10px}
.env-front .small{right:16px;top:34px;text-align:right}
</style>
</head>
<body>
<main class="stage">
  <svg width="0" height="0" style="position:absolute">
    <defs>
      <linearGradient id="swoosh-grad" x1="0" y1="0" x2="1" y2="1">
        <stop offset="0" stop-color="#0b2a6b"/>
        <stop offset=".6" stop-color="#1656c4"/>
        <stop offset="1" stop-color="#4aa3ee"/>
      </linearGradient>
    </defs>
  </svg>

  <!-- Business card: contact side -->
  <section class="sheet card card-back">
    <svg class="swoosh" viewBox="0 0 300 172" preserveAspectRatio="none">
      <path d="M0 0 H26 Q10 86 26 172 H0 Z" fill="url(#swoosh-grad)"/>
      <path d="M26 0 Q10 86 26 172" fill="none" stroke="#4aa3ee" stroke-width="2"/>
    </svg>
    <div class="brand"><span class="brand-dot"></span><span class="brand-name">The Branch Mender</span></div>
    <div class="person"><p class="name">Wade Pellow</p><p class="title">President</p></div>
    <ul class="contacts">
      <li><span class="ico"></span>4817 Ransome Ave Suite 100 Des Moines, IA 50321</li>
      <li><span class="ico"></span>Phone 515 • 555 • 0142</li>
      <li><span class="ico"></span>Fax 515 • 555 • 0178</li>
      <li><span class="ico"></span>info@branchmenderpro.com</li>
      <li><span class="ico"></span>www.branchmenderpro.com</li>
    </ul>
  </section>

  <!-- Business card: logo side -->
  <section class="sheet card card-front">
    <svg class="swoosh" viewBox="0 0 300 172" preserveAspectRatio="none">
      <path d="M0 0 H40 Q8 86 40 172 H0 Z" fill="url(#swoosh-grad)"/>
      <path d="M300 0 H262 Q292 86 262 172 H300 Z" fill="url(#swoosh-grad)"/>
    </svg>
    <div class="lockup">
      <div class="brand"><span class="brand-dot"></span><span class="brand-name">The Branch Mender</span></div>
      <p class="tagline">Tree Care Specialists</p>
    </div>
  </section>

  <!-- Letterhead -->
  <section class="sheet letterhead">
    <svg class="swoosh" viewBox="0 0 400 518" preserveAspectRatio="none">
      <path d="M0 0 H150 Q30 40 22 200 Q18 420 60 518 H0 Z" fill="url(#swoosh-grad)"/>
      <path d="M150 0 Q30 40 22 200 Q18 420 60 518" fill="none" stroke="#4aa3ee" stroke-width="3"/>
      <path d="M400 360 Q380 490 240 518 H400 Z" fill="url(#swoosh-grad)"/>
    </svg>
    <div class="brand"><span class="brand-dot"></span><span class="brand-name">The Branch Mender</span></div>
    <p class="small">4817 Ransome Ave Suite 100<br>Des Moines, IA 50321<br>www.branchmenderpro.com</p>
  </section>

  <!-- Envelope: flap side -->
  <section class="sheet envelope env-back">
    <svg class="swoosh" viewBox="0 0 340 170" preserveAspectRatio="none">
      <path d="M0 0 H340 L200 70 Q170 84 140 70 Z" fill="#eceef1" stroke="#d3d7dc"/>
      <path d="M0 120 Q10 160 60 170 H0 Z" fill="url(#swoosh-grad)"/>
      <path d="M340 20 Q330 150 250 170 H340 Z" fill="url(#swoosh-grad)"/>
    </svg>
    <div class="brand"><span class="brand-dot"></span><span class="brand-name">The Branch Mender</span></div>
  </section>

  <!-- Envelope: address side -->
  <section class="sheet envelope env-front">
    <svg class="swoosh" viewBox="0 0 340 170" preserveAspectRatio="none">
      <path d="M0 0 H22 Q6 85 22 170 H0 Z" fill="url(#swoosh-grad)"/>
      <path d="M340 100 Q330 160 260 170 H340 Z" fill="url(#swoosh-grad)"/>
    </svg>
    <div class="brand"><span class="brand-dot"></span><span class="brand-name">The Branch Mender</span></div>
    <p class="small">4817 Ransome Ave Suite 100<br>Des Moines, IA 50321</p>
  </section>
</main>
</body>
</html>
```